Brenmoor Group needs a business card

I would like the card to be simple but modern and elegant.
I like black and white.
or black and gold.
we are a private finance lender and also are involved in property and property developments.

please look at the business card photos i provided i would like B.G only one one side and all the other details on the other side use fonts that tie in with my theme.

Industry/Entity Type

Finance

Contact Information for Business Card

Brenmoor Group (B.G) Callum Brenmoor M: 0418396152 E: callumbren@quivomail.com

Font styles to use
Other font styles liked:
• Use fonts that would reflect our business

Colors
000000
ffffff

Requirements
Must have
• one side of details
• other side has either B.G or Brenmoor Group like in the photos provided

```html
<!DOCTYPE html>
<html lang="en">
<head>
<meta charset="utf-8">
<title>Brenmoor Group – Business Card</title>
<link rel="stylesheet" href="https://fonts.googleapis.com/css2?family=Oswald:wght@300;400&display=swap">
<style>
  :root {
    --page-bg: #d9d9d9;
    --card-black: #0b0b0b;
    --silver: #bdbdbd;
    --silver-soft: #8f8f8f;
    --text-light: #e6e6e6;
    --divider: #3a3a3a;
  }
  * { margin: 0; padding: 0; box-sizing: border-box; }
  html, body {
    width: 1200px;
    height: 1200px;
    overflow: hidden;
    background: var(--page-bg);
  }
  .sheet {
    width: 1200px;
    height: 1200px;
    display: flex;
    flex-direction: column;
    align-items: center;
    justify-content: center;
    gap: 60px;
  }
  .card {
    position: relative;
    width: 840px;
    height: 514px;
    border-radius: 4px;
    overflow: hidden;
    background: radial-gradient(ellipse at 55% 45%, #1c1c1c 0%, var(--card-black) 70%);
    box-shadow: 0 10px 28px rgba(0, 0, 0, 0.28);
  }
  .card__texture {
    position: absolute;
    inset: 0;
    background: radial-gradient(ellipse at 60% 50%, rgba(60, 60, 60, 0.35) 0%, rgba(0, 0, 0, 0) 65%);
  }

  /* Details side */
  .card--details .monogram {
    position: absolute;
    left: 80px;
    top: 50%;
    transform: translateY(-50%);
    width: 280px;
    text-align: center;
    font-family: "Oswald", sans-serif;
    font-weight: 300;
    font-size: 150px;
    line-height: 1;
    color: var(--silver);
  }
  .card--details .divider {
    position: absolute;
    left: 392px;
    top: 140px;
    width: 1px;
    height: 240px;
    background: var(--divider);
  }
  .contact {
    position: absolute;
    left: 428px;
    top: 172px;
    font-family: "Oswald", sans-serif;
    font-weight: 300;
    color: var(--text-light);
  }
  .contact__name {
    font-size: 40px;
    font-weight: 400;
    letter-spacing: 0.5px;
    line-height: 1.2;
    margin-bottom: 20px;
  }
  .contact__line {
    display: flex;
    align-items: center;
    gap: 12px;
    font-size: 27px;
    line-height: 1.3;
    margin-bottom: 10px;
  }
  .contact__icon { width: 26px; height: 26px; flex: none; }

  /* Brand side */
  .card--brand .wordmark {
    position: absolute;
    inset: 0;
    display: flex;
    flex-direction: column;
    align-items: center;
    justify-content: center;
    font-family: "Oswald", sans-serif;
    font-weight: 300;
    font-size: 118px;
    line-height: 1.1;
    color: var(--silver-soft);
    text-align: center;
  }
</style>
</head>
<body>
<main class="sheet">

  <section class="card card--details" aria-label="Business card, details side">
    <div class="card__texture" role="img" aria-label="Subtle dark textured card background"></div>
    <div class="monogram">B.G</div>
    <div class="divider"></div>
    <div class="contact">
      <p class="contact__name">Callum Brenmoor</p>
      <p class="contact__line">
        <svg class="contact__icon" viewBox="0 0 26 26" aria-hidden="true">
          <circle cx="13" cy="13" r="13" fill="var(--text-light)"/>
          <rect x="9" y="6" width="8" height="14" rx="1.5" fill="var(--card-black)"/>
          <rect x="10.5" y="8" width="5" height="7" fill="var(--text-light)"/>
        </svg>
        0418396152
      </p>
      <p class="contact__line">
        <svg class="contact__icon" viewBox="0 0 26 26" aria-hidden="true">
          <circle cx="13" cy="13" r="13" fill="var(--text-light)"/>
          <rect x="6" y="8.5" width="14" height="9" rx="1" fill="var(--card-black)"/>
          <path d="M6.5 9 L13 14 L19.5 9" fill="none" stroke="var(--text-light)" stroke-width="1.2"/>
        </svg>
        callumbren@quivomail.com
      </p>
    </div>
  </section>

  <section class="card card--brand" aria-label="Business card, brand side">
    <div class="card__texture" role="img" aria-label="Subtle dark textured card background"></div>
    <div class="wordmark">
      <span>Brenmoor</span>
      <span>Group</span>
    </div>
  </section>

</main>
</body>
</html>
```